DORLIT HOMES Professional Home Buyers

Please see two files uploaded. One is my new LOGO (thanks Quenby) and the other gives the wording and pages desired. Of course I am open to suggestions to further enhance what I'm about. I don't want testimonials or houses to buy to appear but to have room for them when I'm ready. I am a real estate investor not a licensed real estate agent. For FAQ i want just the questions to appear and when they click on the question the answer appears and when they click on the question again the answer disappears. make sense? When you read my wording and my idea of pages you'll get an idea of what I'm about. Suggestions are welcomed.

Industry/Entity Type

Real Estate

Number of Pages Required

5+ page

Requirements
Must have
• FAQ pages only questions appear. They click on question the answer appears underneath. they click on question again, the answer disappears. Also, I of course, want my new LOGO to appear on each page I don't know if it will look better all by itself or blended in somehow? Call now 418-555-0193 on each page also. I will get a real phone number before website goes live. If you have a better way of wording what I'm describing please let me know, I am open to feedback
Nice to have
• Anything that the average homeowner can relate to (yea I know, that doesn't help you much, right?)
• Testimonial page and houses to buy page could be done with just the shell ready in the wings for when my business grows it will be ready all that it would need then are the wording and pictures to be uploaded onto the website page. make sense?
Should not have
• I don't want it too elegant or rich looking as I believe my audience will be mostly the average homeowner who needs help

```html
<!DOCTYPE html>
<html lang="en">
<head>
<meta charset="utf-8">
<title>DORLIT HOMES – Professional Home Buyers</title>
<link href="https://fonts.googleapis.com/css2?family=Lato:wght@400;700;900&display=swap" rel="stylesheet">
<style>
:root{
  --navy:#1d3566;
  --blue:#2b6cb0;
  --sky:#4b8fd0;
  --ink:#333;
  --muted:#6b6b6b;
  --light:#f1f2f4;
  --line:#d7d9dd;
  --white:#fff;
  --button:#5c5c5c;
}
*{box-sizing:border-box;margin:0;padding:0}
html,body{width:861px;height:1200px;overflow:hidden}
body{font-family:'Lato',sans-serif;color:var(--ink);background:var(--white)}
.page{width:861px;height:1200px;position:relative}

/* header */
.site-header{height:80px;display:flex;align-items:center;padding:0 42px;justify-content:space-between}
.brand{display:flex;align-items:center;gap:8px}
.brand-dot{width:22px;height:22px;border-radius:50%;background:var(--navy)}
.brand-name{font-weight:900;font-size:16px;color:var(--navy);letter-spacing:.5px}
.main-nav{display:flex;gap:4px}
.main-nav a{font-size:10px;color:var(--navy);text-decoration:none;padding:7px 10px;border:1px solid transparent;letter-spacing:.3px}
.main-nav a.active{border-color:var(--navy)}
.header-call{display:flex;align-items:center;gap:6px;color:var(--navy)}
.header-call small{display:block;font-size:9px;color:var(--muted)}
.header-call strong{font-size:14px}

/* hero */
.hero{height:320px;position:relative;background:linear-gradient(120deg,#cfe0f2 0%,#7fa9d6 45%,#2f5f97 100%)}
.hero-caption{position:absolute;left:0;right:0;top:185px;height:80px;background:rgba(10,30,60,.72);color:var(--white);text-align:center;font-size:15px;font-weight:700;line-height:1.45;padding:14px 60px}
.hero-arrow{position:absolute;top:150px;color:var(--white);font-size:26px}
.hero-arrow.left{left:20px}.hero-arrow.right{right:20px}

/* intro */
.intro{height:175px;text-align:center;padding:34px 110px 0}
.intro h2{color:var(--blue);font-size:17px;font-weight:700;margin-bottom:18px}
.intro p{font-size:10.5px;line-height:1.7;color:var(--muted)}
.intro p strong{color:var(--ink)}

/* offers */
.offers{height:215px;display:flex}
.offer{flex:1;position:relative;color:var(--white);text-align:center;padding:34px 40px 0}
.offer.cash{background:linear-gradient(135deg,#3a3326,#5b4a33)}
.offer.sell{background:linear-gradient(135deg,#4c5a3a,#6c6b5a)}
.offer::before{content:"";position:absolute;inset:0;background:rgba(0,0,0,.35)}
.offer>*{position:relative}
.offer h3{font-size:15px;font-weight:700;margin:8px 0 10px}
.offer p{font-size:9.5px;line-height:1.6}
.offer ul{list-style:none;text-align:left;display:inline-grid;grid-template-columns:auto auto;gap:4px 22px;font-size:10px}
.offer li::before{content:"✓ ";}
.btn{display:inline-block;background:var(--button);color:var(--white);font-size:11px;font-weight:700;padding:9px 20px;margin-top:14px}

/* quote */
.quote{height:290px;background:var(--light);padding:24px 120px 0}
.quote h2{text-align:center;color:var(--blue);font-size:17px;margin-bottom:20px}
.form-grid{display:grid;grid-template-columns:1fr 1fr;gap:12px 30px}
.field{height:26px;background:var(--white);border:1px solid var(--line);font-size:9px;color:#999;padding:8px}
.split{display:grid;grid-template-columns:1fr 1fr;gap:10px}
.submit{display:block;margin:18px auto 0;width:70px;background:var(--navy);color:var(--white);font-size:10px;font-weight:700;text-align:center;padding:8px 0}

/* footer */
.site-footer{position:absolute;left:0;right:0;bottom:0;height:130px;background:var(--navy);color:var(--white);padding:20px 60px}
.footer-nav{display:flex;gap:16px;font-size:9px;letter-spacing:.4px}
.footer-row{display:flex;align-items:center;gap:36px;margin-top:16px}
.footer-row .brand-name{color:var(--white);font-size:13px}
.footer-row .brand-dot{background:var(--white)}
.contact small{display:block;font-size:9px;opacity:.8}
.contact span{font-size:10px}
.social{position:absolute;right:60px;top:40px;display:flex;gap:6px}
.social i{width:20px;height:20px;border-radius:50%;background:var(--white);display:block}
.copy{font-size:8.5px;opacity:.7;margin-top:14px}
</style>
</head>
<body>
<div class="page">
  <header class="site-header">
    <div class="brand"><span class="brand-dot"></span><span class="brand-name">DORLIT HOMES</span></div>
    <nav class="main-nav">
      <a class="active">HOME</a><a>ABOUT US</a><a>FAQ</a><a>CONTACT US</a><a>TESTIMONIALS</a><a>HOUSES TO BUY</a>
    </nav>
    <div class="header-call">
      <svg width="18" height="18" viewBox="0 0 24 24"><path fill="#1d3566" d="M6.6 10.8a15 15 0 006.6 6.6l2.2-2.2a1 1 0 011-.25 11.4 11.4 0 003.6.6 1 1 0 011 1V20a1 1 0 01-1 1A17 17 0 013 4a1 1 0 011-1h3.5a1 1 0 011 1c0 1.25.2 2.45.57 3.57a1 1 0 01-.25 1z"/></svg>
      <div><small>Call Now</small><strong>418-555-0193</strong></div>
    </div>
  </header>

  <section class="hero" role="img" aria-label="Hand in a suit holding a glowing house above a city skyline">
    <span class="hero-arrow left">‹</span><span class="hero-arrow right">›</span>
    <p class="hero-caption">DORLIT HOMES Buys Houses Quickly, In Any Price Range, In Any Condition "as is". We Have Helped People Just Like You In All Kinds Of Situations.</p>
  </section>

  <section class="intro">
    <h2>We Buy Houses In Any Condition!</h2>
    <p>Don't worry whether you need expensive repairs – DORLIT HOMES is currently buying houses throughout the region. We buy houses "as is", we pay cash, we handle all traditional closing costs and we can close in as little as a week. <strong>Contact us today for your free, no obligation quote.</strong></p>
  </section>

  <section class="offers">
    <div class="offer cash" role="img" aria-label="House exterior at dusk">
      <svg width="30" height="24" viewBox="0 0 30 24"><rect x="2" y="5" width="26" height="14" rx="2" fill="none" stroke="#fff" stroke-width="2"/><circle cx="15" cy="12" r="3.5" fill="#fff"/></svg>
      <h3>Get Cash For Your House!</h3>
      <p>DORLIT HOMES can help you avoid foreclosure, stop paying costly repairs, skip agent fees and move on with your life. Get a fair cash offer today.</p>
      <span class="btn">Get Started</span>
    </div>
    <div class="offer sell" role="img" aria-label="Family home with a front garden">
      <svg width="26" height="24" viewBox="0 0 26 24"><path d="M3 12 13 3l10 9M6 10v11h14V10" fill="none" stroke="#fff" stroke-width="2"/></svg>
      <h3>Sell Your Home Fast!</h3>
      <ul><li>We pay all cash</li><li>We pay closing costs</li><li>We buy "as is"</li><li>No fees or commissions</li><li>Quick closings</li></ul>
      <br><span class="btn">Get Started</span>
    </div>
  </section>

  <section class="quote">
    <h2>Get Your Free Quote</h2>
    <div class="form-grid">
      <div class="field">First Name</div><div class="field">Property Address</div>
      <div class="field">Last Name</div><div class="split"><div class="field">City</div><div class="field">State</div></div>
      <div class="split"><div class="field">Phone</div><div class="field">Cell</div></div><div class="split"><div class="field">Zip</div><div class="field">Bedrooms</div></div>
      <div class="field">E-mail</div><div class="field">Asking Price</div>
    </div>
    <span class="submit">SUBMIT</span>
  </section>

  <footer class="site-footer">
    <nav class="footer-nav"><span>HOME</span><span>ABOUT US</span><span>FAQ</span><span>CONTACT US</span><span>TESTIMONIALS</span><span>HOUSES TO BUY</span></nav>
    <div class="footer-row">
      <div class="contact"><small>DORLIT HOMES</small><span>48 Maple Row, Brookvale</span></div>
      <div class="contact"><small>Call Us</small><span>418-555-0193</span></div>
      <div class="contact"><small>Email Us</small><span>info@dorlithomes.com</span></div>
      <div class="brand"><span class="brand-dot"></span><span class="brand-name">DORLIT HOMES</span></div>
    </div>
    <div class="social"><i></i><i></i><i></i></div>
    <p class="copy">© 2024 Dorlit Homes. All Rights Reserved.</p>
  </footer>
</div>
</body>
</html>
```